New Website Design for Rides for Heroes.org - A Site for People to Donate Cars to War / Disabled Ve

Current site: www.ridesforheroes.org; Look at these sites for ideas: bykes2tots.org; motorsfordreams.org; www.autosforourcadets.org; www.trucksforheroes.org

Industry/Entity Type

Charity

Coding

Coded - Design and coding required

Number of Pages Required

1 page

Requirements
Must have
• n/a
Nice to have
• n/a
Should not have
• n/a

```html
<!DOCTYPE html>
<html lang="en">
<head>
<meta charset="utf-8">
<title>Trucks for Heroes – How To Donate A Vehicle</title>
<link href="https://fonts.googleapis.com/css2?family=Roboto:ital,wght@0,300;0,400;0,500;1,300&display=swap" rel="stylesheet">
<style>
:root{
  --sky:#8db4d9;
  --navy:#2c5a80;
  --footer:#264a6b;
  --orange:#d5773a;
  --field:#f1f1f1;
  --label:#254a6e;
  --white:#ffffff;
  --placeholder:#b5b5b5;
  --photo-a:#8a6a58;
  --photo-b:#c9b8ab;
}
*{box-sizing:border-box;margin:0;padding:0}
html,body{width:1130px;height:1200px;overflow:hidden}
body{background:var(--sky);font-family:'Roboto',sans-serif;position:relative}
.main-nav{position:absolute;top:92px;left:205px;display:flex;gap:2px}
.main-nav a{display:flex;align-items:center;justify-content:center;height:42px;background:var(--navy);color:var(--white);font-size:12px;font-weight:500;text-decoration:none;border-radius:8px}
.main-nav a.current{background:var(--orange);height:40px}
.donation-form{position:absolute;left:211px;top:187px;width:290px}
.field{margin-bottom:17px}
.field label{display:block;color:var(--label);font-size:14px;font-weight:500;margin:0 0 4px 14px}
.field .input{height:34px;background:var(--field);border-radius:3px;padding:7px 9px;font-size:12px;font-style:italic;font-weight:300;color:var(--placeholder)}
.field .input.message{height:80px}
.submit{margin-top:13px;width:130px;height:30px;background:var(--orange);color:var(--white);font-size:14px;font-weight:500;display:flex;align-items:center;justify-content:center;border-radius:2px}
.intro{position:absolute;left:571px;top:234px;width:485px;color:var(--white)}
.intro h1{font-size:30px;font-weight:400;margin-bottom:18px}
.intro p{font-size:14px;line-height:18px;margin-bottom:18px}
.campaign{position:absolute;left:571px;top:554px;width:481px}
.campaign .photo{height:209px;background:linear-gradient(120deg,var(--photo-a),var(--photo-b))}
.campaign .cta{height:52px;background:var(--orange);color:var(--white);display:flex;align-items:center}
.cta .join{width:280px;text-align:center;font-size:14px;line-height:17px}
.cta .now{font-size:23px;font-weight:300}
.campaign .total{height:52px;background:var(--white);display:flex;align-items:center;justify-content:center;font-size:24px;font-weight:300;color:#5878b8}
.total span{color:var(--orange);margin-left:6px}
.site-footer{position:absolute;left:0;top:954px;width:1130px;height:246px;background:var(--footer);color:var(--white)}
.footer-col{position:absolute;top:40px}
.footer-col h2{display:inline-block;font-size:22px;font-weight:400;padding-bottom:4px;border-bottom:2px solid var(--orange);margin-bottom:12px}
.footer-col p{font-size:12px;line-height:16px}
.contact{left:48px;width:285px}
.nonprofit{left:407px;width:280px}
.connect{left:760px;width:262px;text-align:center}
.connect .phone{font-size:24px;margin-top:-2px}
.social{display:flex;gap:18px;justify-content:center;margin-top:26px}
.social span{width:50px;height:50px;display:block}
</style>
</head>
<body>
<nav class="main-nav">
  <a href="#" style="width:142px">HOME</a>
  <a href="#" style="width:146px">ABOUT</a>
  <a href="#" style="width:245px">WHY DONATE YOUR CAR</a>
  <a href="#" class="current" style="width:290px">HOW TO DONATE YOUR VEHICLE</a>
</nav>

<form class="donation-form">
  <div class="field"><label>Name:</label><div class="input">Enter Name</div></div>
  <div class="field"><label>Email:</label><div class="input">Enter Email</div></div>
  <div class="field"><label>Company:</label><div class="input">Enter Company</div></div>
  <div class="field"><label>Work Address:</label><div class="input">Enter Address</div></div>
  <div class="field"><label>City:</label><div class="input">Enter City</div></div>
  <div class="field"><label>State:</label><div class="input">Enter State</div></div>
  <div class="field"><label>Zip code:</label><div class="input">Enter Zip</div></div>
  <div class="field"><label>Country:</label><div class="input">Enter Country</div></div>
  <div class="field"><label>Message:</label><div class="input message">Enter Your Message</div></div>
  <div class="submit">Submit</div>
</form>

<section class="intro">
  <h1>How To Donate A Vehicle</h1>
  <p>Trucks for Heroes is Ride Giving Trust's tax-exempt vehicle donation program that benefits disabled veterans. Our car donation program accepts cars, boats (with trailer), RVs, trucks, SUVs, and motorcycles, whether they are running or not. At no cost to you, we will arrange to have your vehicle towed away at a scheduled time that is best for you and your preliminary tax receipt will be mailed to you within 15 days.</p>
  <p>On rare occasion, we find that some vehicles, primarily boats and RVs, are not cost-effective. This will hinder our main goal, which is helping disabled veterans. We do our absolute best to make the most of every vehicle donated, but reserve the right to turn down a vehicle donation for any reason. Please call us at 1-855-555-0148 with any questions regarding your donation. Thank you for your understanding</p>
</section>

<section class="campaign">
  <div class="photo" role="img" aria-label="A soldier lifting a smiling baby in front of a national flag"></div>
  <div class="cta"><div class="join">JOIN OUR<br>CAMPAIGN</div><div class="now">Donate now! &gt;</div></div>
  <div class="total">Donate so far<span>$600 000</span></div>
</section>

<footer class="site-footer">
  <div class="footer-col contact">
    <h2>CONTACT INFORMATION</h2>
    <p>For immediate scheduling of your vehicle donation, please call 1-811-555-0123. Experienced representatives are available anytime day or night to assist you with the entire transaction.</p>
  </div>
  <div class="footer-col nonprofit">
    <h2>WE ARE A NON-PROFIT</h2>
    <p>Trucks for Heroes is Ride Giving Trust's vehicle donation program. Ride Giving Trust is a tax exempt charity under section 501(c)(3) of the IRS Code. Ride Giving Trust donates proceeds from its Trucks for Heroes program to other tax exempt charities that help disabled veterans.</p>
  </div>
  <div class="footer-col connect">
    <h2>CONNECT WITH US</h2>
    <div class="phone">1-811-555-0123</div>
    <div class="social">
      <span style="background:#3b5998" aria-label="Social link"></span>
      <span style="background:#2fa9e0" aria-label="Social link"></span>
      <span style="background:#e8763a" aria-label="Feed link"></span>
      <span style="background:#c8373a" aria-label="Social link"></span>
    </div>
  </div>
</footer>
</body>
</html>
```